WebSite Revamp / Modernize / stylize to draw in more customers to stay on site

Keel-Deck is looking for a website revamp - we had our old site for some time and now is the time for an update - current site - http://www.keel-deck-example.com/ For additional photos, head to the facebook page - https://www.facebook.com/keeldeckexample / I attached the entire current website as well - looking for something modern and bold that has guy appeal - this is not a cheap product and would like site to have that feel as well.

Target Market(s)

Fishermen, fishing guides, homeowners, boat owners

Coding

Coded - Design and coding required

Number of Pages Required

5+ page

Font styles to use
Serif
Sans Serif
Other font styles liked:
• logo font is "Niamey Medium"

Colors
3176b5
0255a3
3276b5
0692cd
33a6d7
85cae6
cee9f5
b1b1b1
d5d5d5

Requirements
Must have
• Keep colors inline with our logo (blues / greys). Also, need it to be relatively easy to add and remove new locations as they come online - we are franchising and starting to add new locations pretty quickly - need this to be an easy process/update to the site.
Nice to have
• Surprise me

```html
<!DOCTYPE html>
<html lang="en">
<head>
<meta charset="utf-8">
<title>Keel-Deck – High Performance Marine Surfacing</title>
<link href="https://fonts.googleapis.com/css2?family=Open+Sans:wght@400;600;700;800&display=swap" rel="stylesheet">
<style>
:root{
  --blue:#0692cd;
  --blue-dark:#0255a3;
  --blue-mid:#3176b5;
  --blue-light:#85cae6;
  --blue-pale:#cee9f5;
  --grey:#b1b1b1;
  --grey-light:#eef1f3;
  --text:#333;
  --muted:#666;
  --orange:#f6a21a;
  --white:#fff;
}
*{box-sizing:border-box;margin:0;padding:0}
html,body{width:1200px;height:2328px;overflow:hidden}
body{font-family:"Open Sans",Arial,sans-serif;color:var(--text);background:var(--white)}
.wrap{width:720px;margin:0 auto;position:relative}

/* header */
.site-header{height:68px;display:flex;align-items:center}
.site-header .wrap{display:flex;align-items:center;justify-content:space-between;width:1040px}
.brand{display:flex;align-items:center;gap:8px;font-weight:800;font-size:20px;color:var(--blue-dark);line-height:1.1}
.brand-mark{width:16px;height:16px;border-radius:50%;background:var(--blue)}
.brand small{display:block;font-size:8px;font-weight:600;color:var(--muted)}
.header-contacts{display:flex;gap:40px;font-size:10px;color:var(--muted);text-align:center}
.header-contacts b{display:block;color:var(--blue-dark);font-size:11px}
.btn-quote-sm{background:var(--blue);color:var(--white);font-size:11px;font-weight:700;padding:7px 14px}

.main-nav{height:28px;background:var(--blue)}
.main-nav ul{list-style:none;display:flex;width:1040px;margin:0 auto;height:100%}
.main-nav li{color:var(--white);font-size:9px;font-weight:700;text-transform:uppercase;padding:0 22px;display:flex;align-items:center}
.main-nav li.active{background:var(--blue-dark)}

/* hero */
.hero{height:504px;position:relative;
  background:
    radial-gradient(ellipse 38% 55% at 66% 30%,rgba(255,255,255,.95),rgba(255,255,255,0) 70%),
    radial-gradient(ellipse 30% 40% at 20% 20%,rgba(245,246,247,.9),rgba(245,246,247,0) 70%),
    radial-gradient(ellipse 70% 45% at 50% 100%,#5e666b,rgba(94,102,107,0) 75%),
    radial-gradient(ellipse 40% 35% at 85% 80%,#737c81,rgba(115,124,129,0) 70%),
    linear-gradient(180deg,#d7dadc 0%,#c3c8cb 45%,#8d969b 75%,#6f787d 100%)}
.hero-arrow{position:absolute;top:238px;width:20px;height:28px;background:rgba(0,0,0,.35);display:flex;align-items:center;justify-content:center}
.hero-arrow.left{left:0}.hero-arrow.right{right:0}

/* feature cards */
.features{background:var(--grey-light);height:160px;padding-top:34px}
.features .wrap{display:flex;gap:14px}
.feature-card{flex:1;background:var(--white);height:92px;padding:14px 16px;box-shadow:0 1px 3px rgba(0,0,0,.1)}
.feature-card svg{display:block;margin-bottom:4px}
.feature-card h3{font-size:15px;font-weight:700;color:var(--blue-dark);line-height:1.3}
.feature-card p{font-size:10px;color:var(--muted)}

.quote-strip{height:76px;display:flex;align-items:center}
.quote-strip .wrap{display:flex;justify-content:space-between;align-items:center}
.quote-strip p{font-size:11px;font-weight:700;text-transform:uppercase}
.btn-quote{background:var(--orange);color:var(--white);font-size:12px;font-weight:700;padding:10px 20px}

/* about */
.about{background:var(--grey-light);height:580px;padding-top:54px}
.about .wrap{display:flex;gap:24px}
.about-photo{width:232px;height:188px;flex:none;
  background:radial-gradient(ellipse 50% 40% at 50% 60%,#e9ecee,rgba(233,236,238,0) 70%),linear-gradient(150deg,#5f6a70,#aab2b6 55%,#7c868b)}
.about h2{font-size:22px;font-weight:700;margin-bottom:10px;line-height:1.2}
.about p{font-size:11px;line-height:1.65;color:var(--muted);margin-bottom:10px}
.about ul{list-style:disc;padding-left:14px}
.about li{font-size:11px;line-height:1.65;color:var(--muted);margin-bottom:7px}
.about li b{color:var(--text)}

/* services */
.services{height:604px;padding-top:58px}
.services h2{text-align:center;font-size:15px;font-weight:700;margin-bottom:50px}
.service-grid{display:flex;gap:20px;justify-content:center}
.service-card{width:350px;height:400px;background:var(--white);box-shadow:0 1px 4px rgba(0,0,0,.12);padding:0 20px 20px}
.service-photo{width:120px;height:120px;border-radius:50%;margin:-6px auto 20px}
.service-photo.marine{background:radial-gradient(circle,#c2c9cc,#6e7a80)}
.service-photo.home{background:radial-gradient(circle,#b5513f,#7a2a20)}
.service-card h3{font-size:16px;font-weight:700;margin-bottom:10px}
.service-card p{font-size:11px;line-height:1.75;color:var(--muted)}

/* footer */
.site-footer{background:var(--blue);height:272px;color:var(--white);padding-top:28px}
.site-footer .wrap{display:flex;justify-content:space-between}
.locations{font-size:10px;line-height:1.45}
.location{margin-bottom:16px}
.location b{display:block}
.connect{display:flex;gap:6px;align-items:flex-start;font-size:10px;padding-top:40px}
.connect .dot{width:10px;height:10px;background:var(--white);opacity:.8;border-radius:2px}
.contact-form{width:240px}
.contact-form label{display:block;font-size:8px;margin-bottom:2px}
.field{background:var(--white);height:16px;margin-bottom:6px}
.field.msg{height:110px}
.btn-submit{display:inline-block;background:#1d2a38;color:var(--white);font-size:8px;padding:4px 10px;margin-top:4px}
.footer-bottom{background:var(--blue-dark);height:28px;color:var(--blue-pale);font-size:8px;display:flex;align-items:center}
</style>
</head>
<body>

<header class="site-header">
  <div class="wrap">
    <div class="brand"><span class="brand-mark"></span><div>Keel-Deck<small>High Performance Marine Surfacing</small></div></div>
    <div class="header-contacts">
      <div><b>Harbor Point, TX</b>555-014-2201</div>
      <div><b>Email Us</b>info@keel-deck-example.com</div>
      <div><b>Bay Landing, FL</b>555-014-2202</div>
    </div>
    <div class="btn-quote-sm">Get a Quote</div>
  </div>
</header>

<nav class="main-nav">
  <ul>
    <li class="active">Home</li><li>About</li><li>Marine Flooring</li><li>Residential Flooring</li><li>Gallery</li><li>FAQ</li><li>Blog</li><li>Testimonials</li><li>Contact</li>
  </ul>
</nav>

<section class="hero" role="img" aria-label="Photo of a boat deck finished with grey speckled non-skid marine surfacing beside a white console">
  <div class="hero-arrow left"><svg width="8" height="12"><path d="M7 1L2 6l5 5" stroke="#fff" stroke-width="2" fill="none"/></svg></div>
  <div class="hero-arrow right"><svg width="8" height="12"><path d="M1 1l5 5-5 5" stroke="#fff" stroke-width="2" fill="none"/></svg></div>
</section>

<section class="features">
  <div class="wrap">
    <div class="feature-card">
      <svg width="22" height="22" viewBox="0 0 22 22"><rect x="3" y="2" width="16" height="18" fill="none" stroke="#0692cd" stroke-width="2"/><path d="M7 8h8M7 12h8M7 16h5" stroke="#0692cd" stroke-width="2"/></svg>
      <h3>Blog</h3><p>Read the latest from our crew</p>
    </div>
    <div class="feature-card">
      <svg width="22" height="22" viewBox="0 0 22 22"><rect x="2" y="4" width="18" height="14" fill="none" stroke="#0692cd" stroke-width="2"/><path d="M4 16l5-6 4 4 3-3 3 5" stroke="#0692cd" stroke-width="2" fill="none"/></svg>
      <h3>Gallery</h3><p>View images of our best work</p>
    </div>
    <div class="feature-card">
      <svg width="22" height="22" viewBox="0 0 22 22"><path d="M4 18l2-6L16 2l4 4-10 10z" fill="none" stroke="#0692cd" stroke-width="2"/></svg>
      <h3>Contact Us</h3><p>Write us a message</p>
    </div>
  </div>
</section>

<section class="quote-strip">
  <div class="wrap">
    <p>For a guaranteed price on any of our products and services</p>
    <div class="btn-quote">Get a Quote</div>
  </div>
</section>

<section class="about">
  <div class="wrap">
    <div class="about-photo" role="img" aria-label="Photo of a boat interior coated in grey non-skid flooring"></div>
    <div>
      <h2>What is Keel-Deck® High Performance<br>Marine Surfacing?</h2>
      <p>Keel-Deck is a poured polymer surface that bonds to fiberglass, aluminum and wood decks. It gives anglers a sure footing, stays cool in the sun and holds up to years of salt, fuel and hard use on the water.</p>
      <p>Every job is finished by trained installers who prep, prime and apply each layer by hand, so the surface fits the lines of your boat and lasts for seasons to come.</p>
      <ul>
        <li><b>Prevents slips, falls and injuries.</b> The textured finish grips wet boots and bare feet alike, keeping crews steady in rough chop.</li>
        <li><b>Cushions fatigue.</b> The flexible layer softens each step, so long days standing at the rail feel easier on the legs.</li>
        <li><b>Dampens sound and noise.</b> Dropped gear and tackle land quietly, keeping fish from being spooked.</li>
        <li><b>Enhances the appearance and value of your boat.</b> A clean, seamless deck in a range of colors raises resale value.</li>
        <li><b>Environmentally safe.</b> Made with low-odor materials that are safe for crews and marine life.</li>
      </ul>
    </div>
  </div>
</section>

<section class="services">
  <h2>What we do</h2>
  <div class="wrap">
    <div class="service-grid">
      <div class="service-card">
        <div class="service-photo marine" role="img" aria-label="Photo of a finished marine deck"></div>
        <h3>Marine Flooring</h3>
        <p>Our surface is the ultimate in non-skid protection for center consoles, bay boats and pontoons. It is built to handle hooks, fish and spills while giving every deck a clean, custom look that stands out at the dock. There is no tape, no glue and no seams to lift, trap water or peel away over time.</p>
      </div>
      <div class="service-card">
        <div class="service-photo home" role="img" aria-label="Photo of a residential patio floor"></div>
        <h3>Residential Flooring</h3>
        <p>Bring the same tough finish home to pool decks, patios, garages and porches. It stays cool underfoot, resists stains and gives families a safe place to walk when the ground is wet. Pick a color and texture to match your home.</p>
      </div>
    </div>
  </div>
</section>

<footer class="site-footer">
  <div class="wrap">
    <div class="locations">
      <div class="location"><b>Harbor Point, TX</b>555-014-2201</div>
      <div class="location"><b>Bay Landing, FL</b>555-014-2202</div>
      <div class="location"><b>Gulf Shores, AL</b>555-014-2203</div>
    </div>
    <div class="connect">Connect with us <span class="dot"></span><span class="dot"></span></div>
    <div class="contact-form">
      <label>Name</label><div class="field"></div>
      <label>Email</label><div class="field"></div>
      <label>Message</label><div class="field msg"></div>
      <div class="btn-submit">Submit</div>
    </div>
  </div>
</footer>
<div class="footer-bottom"><div class="wrap">© 2024 Keel-Deck. All rights reserved.</div></div>

</body>
</html>
```